Save The Date for 2019 RLX Colloquium

We have an annual meeting each June and need a Save the Date (STD) designed. It should be a two-sided postcard with room for address and stamp (according to US Mail postal standards). I have attached some examples from prior years, but we would appreciate a more modern and attractive design for this year's STD.

Target Market(s)

Our own members - nurses, nurse practitioners, PAs and physicians

Industry/Entity Type

Medical

Requirements
Must have
• Must include our logos (attached), ideally in a coordinating fashion - as was done in prior years (see examples attached) and without modifying the logos too much. Needs have the following information:
• - "Save the Date"
• - "The 12th Annual Heartline Crew Colloquium"
• - "Friday, June 7, 2019" or "6/7/19"
• - "The Varrick–Dunmore Building | 318 West 57th Street | NYC"
• - Please include our website (www.qb-zrh.org/events), phone number (212-555-0147) and email address (ask@qb-zrh.org) for people to ask questions
• - Must have space for a postage stamp and the name/address of the postcard recipient
Nice to have
• Would be nice to remain in our blue/grey/olive color palate (see attached Brand Standards guide).
Should not have
• Please do not use stock photos of medical staff. Please don't use cartoons or cartoon images (although a tasteful sketch may be considered).

```html
<!DOCTYPE html>
<html lang="en">
<head>
<meta charset="utf-8">
<title>Save the Date – 2019 RLX Colloquium</title>
<link rel="stylesheet" href="https://fonts.googleapis.com/css2?family=Libre+Baskerville:wght@400;700&family=Montserrat:wght@400;500;600;700&display=swap">
<style>
  :root {
    --navy: #123c7c;
    --navy-deep: #0d2f66;
    --sky: #1b8ccb;
    --sky-light: #4fb0e3;
    --ink: #3a4a60;
    --white: #ffffff;
    --stamp: #d9d9d9;
    --rule: #b9c1cc;
    --backdrop: #eceff2;
  }
  * { box-sizing: border-box; margin: 0; padding: 0; }
  html, body { width: 1200px; height: 912px; overflow: hidden; background: var(--backdrop); }
  body { position: relative; font-family: "Montserrat", sans-serif; color: var(--ink); }

  .postcard {
    position: absolute; top: 269px; width: 560px; height: 374px;
    background: var(--white); overflow: hidden;
    box-shadow: 0 6px 18px rgba(0,0,0,.18);
  }
  .postcard--front { left: 30px; }
  .postcard--back { left: 610px; }

  /* Front */
  .headline {
    position: absolute; left: 22px; top: 24px;
    font-family: "Libre Baskerville", serif; font-weight: 700;
    font-size: 33px; letter-spacing: 1px; color: var(--navy);
  }
  .event-band {
    position: absolute; left: 0; top: 72px; width: 350px; height: 102px;
    background: var(--sky); color: var(--white); padding: 10px 0 0 22px;
    text-transform: uppercase;
  }
  .event-band__title { font-weight: 700; font-size: 23px; line-height: 1; letter-spacing: .5px; }
  .event-band__subtitle { font-weight: 600; font-size: 11.5px; margin-top: 4px; }
  .event-band__second { font-weight: 700; font-size: 20px; margin-top: 9px; line-height: 1; }
  .event-band__second span { text-transform: none; }
  .event-band__subtitle2 { font-weight: 600; font-size: 11.5px; margin-top: 3px; }

  .heart-sketch {
    position: absolute; left: 352px; top: 14px; width: 190px; height: 222px;
    background: radial-gradient(ellipse at 55% 55%, #6f8fbf 0%, #2f568f 55%, #dfe6f0 100%);
    border-radius: 46% 40% 48% 44%;
  }

  .event-date {
    position: absolute; left: 22px; top: 184px;
    font-weight: 700; font-size: 19px; color: var(--navy); text-transform: uppercase; letter-spacing: .5px;
  }
  .venue {
    position: absolute; left: 22px; top: 210px; font-size: 14.5px; line-height: 1.25; color: var(--ink);
  }

  .contact-band {
    position: absolute; left: 0; bottom: 0; width: 100%; height: 84px; background: var(--navy);
  }
  .postcard--front .contact-band::before {
    content: ""; position: absolute; right: 0; top: -42px; width: 210px; height: 42px; background: var(--navy);
  }
  .ask-pill {
    position: absolute; left: 0; top: -12px; padding: 5px 18px 5px 22px;
    background: var(--sky-light); color: var(--white); font-weight: 600; font-size: 12px;
    border-radius: 0 14px 14px 0;
  }
  .contact-list { position: absolute; left: 22px; top: 18px; list-style: none; }
  .contact-list li {
    display: flex; align-items: center; gap: 8px;
    color: var(--white); font-size: 13.5px; line-height: 20px;
  }
  .contact-list svg { width: 11px; height: 11px; fill: none; stroke: var(--sky-light); stroke-width: 2; }

  .partner-row {
    position: absolute; right: 18px; top: 0; display: flex; align-items: center; gap: 10px;
  }
  .partner-badge { width: 44px; height: 44px; border-radius: 50%; background: #e8edf5; }
  .chapter-mark { display: flex; align-items: center; gap: 8px; padding-left: 8px; border-left: 1px solid rgba(255,255,255,.6); }
  .chapter-mark__dot { width: 12px; height: 12px; border-radius: 50%; background: var(--white); }
  .chapter-mark__name { font-family: "Libre Baskerville", serif; font-size: 14px; color: var(--white); }

  /* Back */
  .message {
    position: absolute; left: 22px; top: 28px; width: 300px;
    font-size: 10.5px; line-height: 1.35; color: var(--ink);
  }
  .message p + p { margin-top: 7px; }
  .message strong { color: var(--navy); font-weight: 700; }

  .postcard--back .contact-band { width: 320px; height: 84px; }
  .postcard--back .contact-list { top: 18px; }

  .stamp-box { position: absolute; right: 24px; top: 16px; width: 58px; height: 66px; background: var(--stamp); }
  .return-address { position: absolute; left: 340px; top: 62px; font-size: 9px; line-height: 1.35; }
  .return-address .chapter-mark { border-left: none; padding-left: 0; margin-bottom: 4px; }
  .return-address .chapter-mark__dot { background: var(--navy); width: 16px; height: 16px; }
  .return-address .chapter-mark__name { color: var(--navy); font-size: 11px; }
  .address-lines { position: absolute; left: 340px; top: 170px; width: 196px; }
  .address-lines span { display: block; height: 34px; border-bottom: 1px solid var(--rule); }
</style>
</head>
<body>

<section class="postcard postcard--front" aria-label="Postcard front">
  <h1 class="headline">SAVE THE DATE</h1>
  <div class="event-band">
    <p class="event-band__title">The 12th Annual</p>
    <p class="event-band__subtitle">Heartline Crew Colloquium</p>
    <p class="event-band__second">&amp; 3<span>rd</span> Annual</p>
    <p class="event-band__subtitle2">QBZRH Summer Soirèe</p>
  </div>
  <div class="heart-sketch" role="img" aria-label="Engraved sketch of a human heart in navy ink"></div>
  <p class="event-date">Friday, June 7, 2019</p>
  <p class="venue">The Varrick–<br>Dunmore Building<br>318 West 57th Street | NYC</p>
  <div class="contact-band">
    <span class="ask-pill">For people to ask questions</span>
    <ul class="contact-list">
      <li><svg viewBox="0 0 12 12"><path d="M2 1h3l1 3-2 1a6 6 0 0 0 3 3l1-2 3 1v3c-6 0-10-4-10-9z"/></svg>(212) 555-0147</li>
      <li><svg viewBox="0 0 12 12"><rect x="1" y="2.5" width="10" height="7"/><path d="M1 3l5 4 5-4"/></svg>ask@qb-zrh.org</li>
      <li><svg viewBox="0 0 12 12"><circle cx="6" cy="6" r="5"/><path d="M1 6h10M6 1c3 3 3 7 0 10M6 1c-3 3-3 7 0 10"/></svg>www.qb-zrh.org/events</li>
    </ul>
    <div class="partner-row">
      <span class="partner-badge"></span>
      <span class="partner-badge"></span>
      <span class="partner-badge"></span>
      <div class="chapter-mark">
        <span class="chapter-mark__dot"></span>
        <span class="chapter-mark__name">Harbor State Chapter</span>
      </div>
    </div>
  </div>
</section>

<section class="postcard postcard--back" aria-label="Postcard back">
  <div class="message">
    <p>Join us for TWO great events at Alder Ridge Golf Club in the Rochester area this June!</p>
    <p>On June 7th, <strong>The Annual Heartline Crew (RLX) Colloquium</strong>, a unique all-day academic event designed to enhance current knowledge about the etiology, prevention, intervention and management of cardiovascular disease that's now in its 11th year, will take place at the Alder Ridge Golf Club in Pittsford, NY.</p>
    <p>Following the RLX Colloquium, the Harbor State Chapter of the QBZ will host <strong>The Second Annual Summer Soirèe</strong> for all members and friends of QBZRH. Be sure to save the date!</p>
    <p>Questions? Call (212) 555-0147 or send us an email at ask@qb-zrh.org</p>
    <p>Recommended lodging: <strong>The Kestrel Pine Lodge</strong></p>
  </div>
  <div class="contact-band">
    <ul class="contact-list">
      <li><svg viewBox="0 0 12 12"><path d="M2 1h3l1 3-2 1a6 6 0 0 0 3 3l1-2 3 1v3c-6 0-10-4-10-9z"/></svg>(212) 555-0147</li>
      <li><svg viewBox="0 0 12 12"><rect x="1" y="2.5" width="10" height="7"/><path d="M1 3l5 4 5-4"/></svg>ask@qb-zrh.org</li>
      <li><svg viewBox="0 0 12 12"><circle cx="6" cy="6" r="5"/><path d="M1 6h10M6 1c3 3 3 7 0 10M6 1c-3 3-3 7 0 10"/></svg>www.qb-zrh.org/events</li>
    </ul>
  </div>
  <div class="stamp-box" aria-label="Postage stamp area"></div>
  <div class="return-address">
    <div class="chapter-mark">
      <span class="chapter-mark__dot"></span>
      <span class="chapter-mark__name">Harbor State Chapter</span>
    </div>
    <p>480 Larkin Avenue Ste. 1204</p>
    <p>New York, NY 10099</p>
  </div>
  <div class="address-lines" aria-label="Recipient address lines">
    <span></span><span></span><span></span><span></span>
  </div>
</section>

</body>
</html>
```